R & T Summit Construction Business Card ideas

We want a business card to represents our company in a way that looks professional but is also a business card that is unique!

Industry/Entity Type

Construction Company

Contact Information for Business Card

open to all design ideas, just want to be able to see different options to choose from in either color or grayscale.

Requirements
Must have
• Our names and phone numbers
• Nolan Pritchett 512-804-2271
• Curtis Hale 512-693-1804
• Business logo

```html
<!DOCTYPE html>
<html lang="en">
<head>
<meta charset="utf-8">
<title>R &amp; T Summit Construction – Business Card</title>
<link rel="stylesheet" href="https://fonts.googleapis.com/css2?family=Open+Sans:wght@400;600;700&display=swap">
<style>
  :root {
    --page-bg: #e6e7e9;
    --card-bg: #f5f6f7;
    --card-edge: #d3d5d8;
    --ink: #1a1a1a;
    --band-dark: #0b0b0b;
    --band-mid: #2a2b2d;
  }
  * { margin: 0; padding: 0; box-sizing: border-box; }
  html, body {
    width: 1200px;
    height: 970px;
    overflow: hidden;
    background: var(--page-bg);
    font-family: "Open Sans", Arial, sans-serif;
    color: var(--ink);
  }
  .canvas {
    position: relative;
    width: 1200px;
    height: 970px;
  }
  .card {
    position: absolute;
    left: 100px;
    top: 205px;
    width: 1000px;
    height: 560px;
    border-radius: 26px;
    background: var(--card-bg);
    border: 1px solid var(--card-edge);
    overflow: hidden;
    box-shadow: 0 12px 34px rgba(0,0,0,0.12);
  }
  .contacts {
    position: absolute;
    left: 48px;
    top: 80px;
  }
  .person { margin-bottom: 18px; }
  .person-name {
    font-weight: 600;
    font-size: 26px;
    letter-spacing: 0.3px;
    line-height: 1.2;
    text-transform: uppercase;
  }
  .line {
    display: flex;
    align-items: center;
    gap: 8px;
    font-size: 22px;
    line-height: 1.45;
  }
  .line svg { width: 18px; height: 18px; flex: none; fill: var(--ink); }
  .address {
    font-size: 22px;
    line-height: 1.45;
    margin: 8px 0 22px;
  }
  .brand {
    position: absolute;
    left: 510px;
    top: 205px;
    width: 440px;
    display: flex;
    align-items: center;
    gap: 16px;
  }
  .brand-mark {
    width: 54px;
    height: 54px;
    border-radius: 50%;
    background: var(--ink);
    flex: none;
  }
  .brand-name {
    font-weight: 700;
    font-size: 34px;
    line-height: 1.1;
    color: var(--ink);
    text-transform: uppercase;
  }
  .footer-band {
    position: absolute;
    left: 0;
    bottom: 0;
    width: 100%;
    height: 92px;
    background: linear-gradient(180deg, var(--band-mid) 0%, var(--band-dark) 100%);
  }
</style>
</head>
<body>
<main class="canvas">
  <section class="card" aria-label="Business card">
    <div class="contacts">
      <div class="person">
        <p class="person-name">Nolan Pritchett</p>
        <p class="line">
          <svg viewBox="0 0 24 24"><path d="M6.6 10.8a15.1 15.1 0 0 0 6.6 6.6l2.2-2.2a1 1 0 0 1 1-.25 11.4 11.4 0 0 0 3.6.57 1 1 0 0 1 1 1V20a1 1 0 0 1-1 1A17 17 0 0 1 3 4a1 1 0 0 1 1-1h3.5a1 1 0 0 1 1 1c0 1.25.2 2.46.57 3.6a1 1 0 0 1-.25 1z"/></svg>
          512-804-2271
        </p>
      </div>
      <div class="person">
        <p class="person-name">Curtis Hale</p>
        <p class="line">
          <svg viewBox="0 0 24 24"><path d="M6.6 10.8a15.1 15.1 0 0 0 6.6 6.6l2.2-2.2a1 1 0 0 1 1-.25 11.4 11.4 0 0 0 3.6.57 1 1 0 0 1 1 1V20a1 1 0 0 1-1 1A17 17 0 0 1 3 4a1 1 0 0 1 1-1h3.5a1 1 0 0 1 1 1c0 1.25.2 2.46.57 3.6a1 1 0 0 1-.25 1z"/></svg>
          512-693-1804
        </p>
      </div>
      <p class="address">4418 Cedar Ridge Dr Suite 12,<br>Round Rock, TX 78664</p>
      <p class="line">
        <svg viewBox="0 0 24 24"><path d="M2 5h20v14H2z" fill="var(--ink)"/><path d="M3.5 6.5 12 12.5l8.5-6" fill="none" stroke="var(--card-bg)" stroke-width="1.6"/></svg>
        info@rtsummitconstruction.com
      </p>
      <p class="line">
        <svg viewBox="0 0 24 24"><circle cx="12" cy="12" r="9" fill="none" stroke="var(--ink)" stroke-width="2.2"/><path d="M3 12h18M12 3c3 3 3 15 0 18M12 3c-3 3-3 15 0 18" fill="none" stroke="var(--ink)" stroke-width="1.8"/></svg>
        www.rtsummitconstruction.com
      </p>
    </div>

    <div class="brand">
      <span class="brand-mark"></span>
      <p class="brand-name">R &amp; T Summit Construction</p>
    </div>

    <div class="footer-band" role="img" aria-label="Decorative black and silver swoosh band along the card's lower edge"></div>
  </section>
</main>
</body>
</html>
```